" Atendimento ambulatorial com consultas pré ciúrgicas e procedimentos estéticos da face (ex.: toxina botúlínica e preenchimentos faciais) e cirurgias da face em centro cirúrgico (ex.: rinoplastia, otoplastia, blefaroplastia) "

```html
<!DOCTYPE html>
<html lang="pt-BR">
<head>
<meta charset="UTF-8">
<title>Pasta Institucional – Dra. Helena Montavi</title>
<link rel="stylesheet" href="https://fonts.googleapis.com/css2?family=Cinzel:wght@400;600&family=Montserrat:wght@400;500;600&display=swap">
<style>
  :root {
    --page-bg: #ffffff;
    --folder-green: #0e4a42;
    --fold-line: #1d5d54;
    --accent-gold: #b8934a;
    --light: #ffffff;
    --muted-text: #cfe0dc;
  }
  * { margin: 0; padding: 0; box-sizing: border-box; }
  html, body {
    width: 1200px;
    height: 1200px;
    overflow: hidden;
    background: var(--page-bg);
  }
  .canvas {
    position: relative;
    width: 1200px;
    height: 1200px;
  }
  .folder {
    position: absolute;
    left: 132px;
    top: 312px;
    width: 936px;
    height: 576px;
    background: var(--folder-green);
    box-shadow: 0 2px 6px rgba(0,0,0,0.18);
    overflow: hidden;
  }
  .folder__fold {
    position: absolute;
    left: 463px;
    top: 0;
    width: 1px;
    height: 100%;
    background: var(--fold-line);
  }
  .folder__band {
    position: absolute;
    top: 502px;
    height: 8px;
    background: var(--accent-gold);
  }
  .folder__band--left { left: 0; width: 408px; }
  .folder__band--center { left: 415px; width: 96px; background: var(--light); }
  .folder__band--right { left: 520px; width: 416px; }

  .contact-line {
    position: absolute;
    top: 534px;
    font-family: "Montserrat", sans-serif;
    font-size: 11px;
    color: var(--muted-text);
    letter-spacing: 0.3px;
    white-space: nowrap;
  }
  .contact-line--address { left: 36px; }
  .contact-line--district { left: 168px; }
  .contact-line--phone { left: 312px; letter-spacing: 1px; }

  .back-mark {
    position: absolute;
    left: 150px;
    top: 430px;
    display: flex;
    align-items: center;
    gap: 7px;
    font-family: "Cinzel", serif;
    font-weight: 600;
    font-size: 12px;
    color: var(--light);
    letter-spacing: 0.4px;
    white-space: nowrap;
  }
  .back-mark__square {
    width: 12px;
    height: 12px;
    background: var(--accent-gold);
  }

  .brand {
    position: absolute;
    left: 623px;
    top: 356px;
    width: 300px;
    text-align: center;
  }
  .brand__square {
    width: 44px;
    height: 44px;
    margin: 0 auto 30px;
    background: var(--accent-gold);
  }
  .brand__name {
    font-family: "Cinzel", serif;
    font-weight: 600;
    font-size: 16px;
    line-height: 1.1;
    color: var(--light);
    letter-spacing: 0.4px;
    white-space: nowrap;
  }
  .brand__tagline {
    margin-top: 5px;
    font-family: "Montserrat", sans-serif;
    font-weight: 600;
    font-size: 7.5px;
    letter-spacing: 1.4px;
    color: var(--light);
    white-space: nowrap;
  }
</style>
</head>
<body>
  <main class="canvas">
    <section class="folder" aria-label="Pasta institucional aberta">
      <div class="folder__fold"></div>

      <div class="back-mark">
        <span class="back-mark__square"></span>
        <span>Dra. Helena Montavi</span>
      </div>

      <div class="brand">
        <div class="brand__square"></div>
        <div class="brand__name">DRA. HELENA MONTAVI</div>
        <div class="brand__tagline">• CIRURGIA E ESTÉTICA DA FACE •</div>
      </div>

      <div class="folder__band folder__band--left"></div>
      <div class="folder__band folder__band--center"></div>
      <div class="folder__band folder__band--right"></div>

      <span class="contact-line contact-line--address">Rua Endereço, 12345</span>
      <span class="contact-line contact-line--district">Bairro, Cidade, Estado</span>
      <span class="contact-line contact-line--phone">+12 123 456 7890</span>
    </section>
  </main>
</body>
</html>
```